Events By Quellon

Weddings, Corporate, Special Events
Memorable Catering, Personalized Menus, Custom Layout & Designs
Professional Staff, Excellent Service
Our Mission is Turning YOUR Vision into a Reality

Dorrie Quellon, Principal Planner
ph. 202 555-0187 - fax 301-555-0142
Email - eventsbyquellon@mailhaven.net
Web - www.cateringbyquellon.net
cateringbyquellon@Instagram

Target Market(s)

All Brides, Corprate Business, Special Events

Industry/Entity Type

Hospitality

Contact Information for Business Card

clean but affective

Font styles to use
Serif
Sans Serif
Script

Colors

Designer to choose colors to be used in the design.

Requirements
Must have
• logo with tagline using colors that will enhance what
• some pictures of nice table scape, hors d'oevures, upscale foods......
Nice to have
• Event: Something that happens or is regarded as happening, an occurrence especially one of some importance.
Should not have
• Use Logo on both sides

```html
<!DOCTYPE html>
<html lang="en">
<head>
<meta charset="utf-8">
<title>Events By Quellon – Business Card</title>
<link rel="stylesheet" href="https://fonts.googleapis.com/css2?family=Great+Vibes&family=Libre+Baskerville:wght@400;700&family=Lora:wght@400;600&display=swap">
<style>
  :root {
    --backdrop: #ece9e4;
    --card-white: #ffffff;
    --card-beige: #e6dcc3;
    --beige-deep: #d4c7a4;
    --teal: #3fb3b8;
    --teal-soft: #a9dfe2;
    --ink: #1f1f1f;
    --ink-soft: #4a4a4a;
    --grey-ring: #cfcfcf;
    --photo-warm: #d9c48e;
    --photo-light: #eeeadf;
  }
  * { margin: 0; padding: 0; box-sizing: border-box; }
  html, body { width: 1200px; height: 675px; overflow: hidden; }
  body {
    background: var(--backdrop);
    position: relative;
    font-family: "Lora", Georgia, serif;
    color: var(--ink);
  }
  .card {
    position: absolute;
    top: 183px;
    width: 540px;
    height: 309px;
    overflow: hidden;
    box-shadow: 0 6px 18px rgba(0,0,0,0.18);
  }

  /* Front */
  .card-front {
    left: 45px;
    background: linear-gradient(160deg, var(--photo-light), var(--card-beige) 55%, var(--beige-deep));
  }
  .front-stripes { position: absolute; inset: 0; }
  .front-photo {
    position: absolute;
    left: 140px; top: 92px;
    width: 260px; height: 140px;
    border: 5px solid var(--card-white);
    background: linear-gradient(180deg, #f1efe8 0%, #e2d6b6 45%, var(--photo-warm) 100%);
  }
  .front-brand {
    position: absolute;
    left: 0; right: 0; top: 30px;
    display: flex; align-items: center; justify-content: center; gap: 10px;
  }
  .brand-dot {
    width: 22px; height: 22px; border-radius: 50%;
    background: var(--teal);
  }
  .brand-name {
    font-family: "Libre Baskerville", Georgia, serif;
    font-size: 20px;
    color: var(--teal);
    font-weight: 400;
  }
  .front-tagline {
    position: absolute;
    left: 0; right: 0; bottom: 30px;
    text-align: center;
    font-family: "Great Vibes", cursive;
    font-size: 30px;
    color: var(--teal);
  }

  /* Back */
  .card-back { left: 615px; background: var(--card-white); }
  .monogram {
    position: absolute;
    left: 150px; top: 50px;
    width: 230px; height: 250px;
    border-radius: 46% 46% 30% 30%;
    background: radial-gradient(ellipse at 50% 45%, var(--teal-soft) 0%, rgba(169,223,226,0.45) 55%, rgba(255,255,255,0) 75%);
  }
  .holder { position: absolute; right: 40px; top: 28px; text-align: center; }
  .holder-name {
    font-family: "Libre Baskerville", Georgia, serif;
    font-size: 24px; font-weight: 700; letter-spacing: 1px;
  }
  .holder-title { font-size: 14px; color: var(--ink-soft); margin-top: 2px; }
  .contact-list {
    position: absolute; left: 22px; top: 96px;
    list-style: none;
  }
  .contact-item {
    display: flex; align-items: center; gap: 10px;
    font-size: 13px; color: var(--ink-soft);
    height: 28px;
  }
  .contact-item svg { width: 13px; height: 13px; fill: var(--ink); flex: none; }
  .services {
    position: absolute; right: 22px; top: 118px;
    list-style: none; text-align: right;
  }
  .service {
    font-size: 11px; font-weight: 600; color: var(--ink);
    line-height: 19px;
  }
  .service::after {
    content: ""; display: inline-block;
    width: 5px; height: 5px; border-radius: 50%;
    background: var(--ink); margin-left: 8px; vertical-align: middle;
  }
</style>
</head>
<body>

<section class="card card-front" aria-label="Card front">
  <svg class="front-stripes" viewBox="0 0 540 309" aria-hidden="true">
    <g fill="#ffffff" opacity="0.75">
      <rect x="20" y="70" width="14" height="160"/>
      <rect x="48" y="70" width="14" height="160"/>
      <rect x="76" y="70" width="14" height="160"/>
      <rect x="104" y="70" width="14" height="160"/>
      <rect x="422" y="70" width="14" height="160"/>
      <rect x="450" y="70" width="14" height="160"/>
      <rect x="478" y="70" width="14" height="160"/>
      <rect x="506" y="70" width="14" height="160"/>
    </g>
    <rect x="0" y="84" width="540" height="4" fill="#ffffff" opacity="0.85"/>
    <rect x="0" y="238" width="540" height="4" fill="#ffffff" opacity="0.85"/>
  </svg>
  <div class="front-photo" role="img" aria-label="Photo of an elegant banquet hall with set tables and gold chairs"></div>
  <div class="front-brand">
    <span class="brand-dot"></span>
    <span class="brand-name">Events By Quellon</span>
  </div>
  <p class="front-tagline">Events Designed With You In Mind</p>
</section>

<section class="card card-back" aria-label="Card back">
  <div class="monogram" role="img" aria-label="Large soft teal ornamental monogram"></div>

  <div class="holder">
    <h1 class="holder-name">DORRIE QUELLON</h1>
    <p class="holder-title">Principal Planner</p>
  </div>

  <ul class="contact-list">
    <li class="contact-item">
      <svg viewBox="0 0 16 16"><path d="M3 1h3l1.5 4-2 1.2a9 9 0 0 0 4.3 4.3l1.2-2 4 1.5v3a2 2 0 0 1-2 2A13 13 0 0 1 1 3a2 2 0 0 1 2-2z"/></svg>
      202 555-0187
    </li>
    <li class="contact-item">
      <svg viewBox="0 0 16 16"><path d="M4 1h8v4H4zM1 6h14v6h-3v3H4v-3H1zM5 10v4h6v-4z"/></svg>
      301-555-0142
    </li>
    <li class="contact-item">
      <svg viewBox="0 0 16 16"><path d="M1 3h14v10H1zM2 4.5v.5l6 4 6-4v-.5z"/></svg>
      eventsbyquellon@mailhaven.net
    </li>
    <li class="contact-item">
      <svg viewBox="0 0 16 16"><circle cx="8" cy="8" r="7"/><circle cx="8" cy="8" r="3" fill="#fff"/></svg>
      cateringbyquellon@Instagram
    </li>
    <li class="contact-item">
      <svg viewBox="0 0 16 16"><path d="M8 1a7 7 0 1 0 0 14A7 7 0 0 0 8 1zm0 1.3c.9 0 1.9 2 2.1 5H5.9C6.1 4.3 7.1 2.3 8 2.3zM2.4 8.7h2.2c.1 1.9.6 3.5 1.2 4.4A5.7 5.7 0 0 1 2.4 8.7zm0-1.4a5.7 5.7 0 0 1 3.4-4.4c-.6.9-1.1 2.5-1.2 4.4zM8 13.7c-.9 0-1.9-2-2.1-5h4.2c-.2 3-1.2 5-2.1 5zm2.2-.6c.6-.9 1.1-2.5 1.2-4.4h2.2a5.7 5.7 0 0 1-3.4 4.4zm1.2-5.8c-.1-1.9-.6-3.5-1.2-4.4a5.7 5.7 0 0 1 3.4 4.4z"/></svg>
      www.cateringbyquellon.net
    </li>
  </ul>

  <ul class="services">
    <li class="service">Engagement party</li>
    <li class="service">Bridal Shower or Couple's Shower</li>
    <li class="service">Bachelor Party And Bachelorette Party</li>
    <li class="service">Bridesmaid Luncheon And Groomsmen Luncheon</li>
    <li class="service">Welcome Party</li>
    <li class="service">Rehearsal Dinner</li>
    <li class="service">Wedding Ceremony And Reception</li>
    <li class="service">After-Party</li>
    <li class="service">Day-After Brunch</li>
  </ul>
</section>

</body>
</html>
```